Web Site

Target Market(s)

CEOs and International Sales & Marketing Directors of International Companies who wish to expand their business reach to Dubai and the Middle East and are looking for a local professional partner to work with.

Requirements
Must have
• Creativity is key. We don't want the normal standard boxes of text and boxes of pics. Be as creative as you like.
Nice to have
• (This is only a suggestion, we welcome your creativity)
- The center of all pages could be large rotating pictures which display professional corporate men/women working in an office, images of Dubai, the UAE, skyscrapers of business towers in Dubai, ..etc.
- Images should reflect Dubai and the Arab World as a modern, fast-paced, growing modern market - Not Traditional)
Should not have
• Not so colorful, the fewer colors you use, the better.
Not Crammed or Busy
Not Traditional but modern

```html
<!DOCTYPE html>
<html lang="en">
<head>
<meta charset="utf-8">
<title>Quillmere Group</title>
<link rel="stylesheet" href="https://fonts.googleapis.com/css2?family=Arimo:wght@400&family=PT+Serif:wght@400;700&family=Roboto+Condensed:wght@400&family=Tinos&display=swap">
<style>
  :root {
    --ink: #2b2b2b;
    --muted: #6b6b6b;
    --blue: #1f5a8c;
    --blue-deep: #0d4f87;
    --accent: #8a2a22;
    --line: #d8d8d8;
    --white: #ffffff;
  }
  * { margin: 0; padding: 0; box-sizing: border-box; }
  html, body { width: 1200px; height: 1172px; overflow: hidden; background: var(--white); }
  body { position: relative; font-family: "Arimo", Arial, sans-serif; color: var(--ink); }
  .abs { position: absolute; }

  .header { position: absolute; left: 0; top: 0; width: 1200px; height: 124px;
    background: linear-gradient(180deg, #ffffff 0%, #f1f1f1 55%, #e6e6e6 100%); }
  .brand { position: absolute; left: 225px; top: 38px; display: flex; align-items: center; gap: 10px; }
  .brand-mark { width: 14px; height: 14px; background: var(--accent); }
  .brand-name { font-family: "Arimo", Arial, sans-serif; font-weight: 400; font-size: 30px; letter-spacing: 2px; color: var(--ink); white-space: nowrap; }

  .utility-nav { position: absolute; right: 69px; top: 12px; display: flex; font-family: "PT Serif", Georgia, serif; font-size: 14px; color: #555; }
  .utility-nav a { color: inherit; text-decoration: none; padding: 6px 9px; border-left: 1px solid #cfcfcf; }
  .utility-nav a:first-child { background: linear-gradient(#fff, #e2e2e2); border-left: 2px solid #bbb; border-right: 2px solid #bbb; }

  .main-nav { position: absolute; left: 0; top: 124px; width: 1200px; height: 32px;
    background: linear-gradient(#f6f6f6, #dcdcdc); border-top: 1px solid #c9c9c9; border-bottom: 1px solid #bdbdbd; }
  .main-nav ul { list-style: none; position: absolute; left: 212px; top: 0; display: flex; height: 31px; }
  .main-nav li { font-family: "PT Serif", Georgia, serif; font-size: 14px; line-height: 31px; padding: 0 5px; border-right: 1px solid #bdbdbd; color: #333; white-space: nowrap; }
  .main-nav li.current { background: linear-gradient(var(--blue-deep), #0a3f6e); color: var(--white); font-weight: 700; width: 75px; text-align: center; }
  .main-nav li.soft { color: #777; }

  .hero { position: absolute; left: 0; top: 156px; width: 1200px; height: 327px;
    background: radial-gradient(ellipse at 45% 30%, #6a6a6a 0%, #474747 45%, #2f2f2f 100%); }
  .hero-title { position: absolute; left: 209px; top: 56px; font-family: "Tinos", "Times New Roman", serif; font-weight: 400; font-size: 32px; color: var(--white); letter-spacing: -1px; white-space: nowrap; }
  .hero-sub { position: absolute; left: 209px; top: 98px; font-family: "Tinos", "Times New Roman", serif; font-size: 17px; color: #f0f0f0; letter-spacing: -0.3px; white-space: nowrap; }
  .hero-text { position: absolute; left: 209px; top: 151px; font-family: "Roboto Condensed", "Arial Narrow", sans-serif; font-size: 12.5px; line-height: 21px; color: #f2f2f2; white-space: nowrap; }
  .hero-rule { position: absolute; left: 209px; top: 255px; width: 424px; height: 1px; background: linear-gradient(90deg, rgba(255,255,255,0.05), rgba(255,255,255,0.45), rgba(255,255,255,0.05)); }
  .hero-btn { position: absolute; top: 271px; height: 42px; border: 1px solid #1c1c1c; border-radius: 3px;
    background: linear-gradient(#5d5d5d, #2b2b2b); box-shadow: inset 0 1px 0 rgba(255,255,255,0.25);
    color: #eee; font-family: "PT Serif", Georgia, serif; font-size: 17px; display: flex; align-items: center; justify-content: center; white-space: nowrap; }
  .hero-btn.prev { left: 207px; width: 34px; }
  .hero-btn.all { left: 247px; width: 143px; }
  .hero-btn.next { left: 396px; width: 34px; }
  .hero-visual { position: absolute; left: 674px; top: -86px; width: 334px; height: 413px;
    background: linear-gradient(180deg, rgba(255,255,255,0) 0%, #6b87b8 28%, #9fb4d6 60%, #dfe6ee 90%, #b9c7d4 100%); }

  .heading { font-family: "PT Serif", Georgia, serif; font-weight: 400; font-size: 18px; color: #333; top: 536px; white-space: nowrap; }
  .heading.blue { color: var(--blue); }
  .copy { font-family: "Roboto Condensed", "Arial Narrow", sans-serif; font-size: 12px; line-height: 19.9px; color: var(--muted); white-space: nowrap; }
  .copy.top { top: 572px; }
  .copy.bottom { top: 831px; }
  .tab { top: 671px; width: 122px; height: 28px; background: linear-gradient(#9a9a9a, #6e6e6e);
    color: var(--white); font-size: 14px; line-height: 28px; padding-left: 10px; white-space: nowrap; }
  .photo { top: 699px; width: 243px; height: 116px; border-top: 4px solid #8a8a8a; }
  .photo.team { background: linear-gradient(180deg, #d9dce2 0%, #bfc4cc 45%, #5a5f68 100%); }
  .photo.deal { background: linear-gradient(160deg, #e9eef4 0%, #b9c3cf 45%, #5f6670 80%, #a36a4a 100%); }
  .divider { top: 557px; width: 1px; height: 437px; background: var(--line); }
  .read-more { top: 941px; width: 125px; height: 43px; border: 1px solid #111; border-radius: 3px;
    background: linear-gradient(#5a5a5a, #1f1f1f); box-shadow: inset 0 1px 0 rgba(255,255,255,0.3);
    color: #eee; font-family: "Tinos", "Times New Roman", serif; font-size: 18px; text-align: center; line-height: 41px; }

  .services { list-style: none; left: 779px; top: 571px; }
  .services li { position: relative; padding-left: 23px; font-size: 19px; line-height: 31.6px; color: #444; white-space: nowrap; }
  .services li::before { content: ""; position: absolute; left: 5px; top: 12px; width: 9px; height: 9px; border-radius: 50%; background: var(--accent); }
  .services li.cont::before { display: none; }
  .services-rule { left: 781px; top: 836px; width: 220px; height: 2px; background: var(--line); }
  .contact-row { left: 783px; font-size: 13.5px; color: #777; white-space: nowrap; }
  .contact-row span { position: absolute; left: 84px; color: #666; }

  .footer { position: absolute; left: 0; top: 1066px; width: 1200px; height: 106px;
    background: linear-gradient(#202020, #3a3a3a 40%, #2e2e2e); }
  .footer-name { position: absolute; left: 210px; top: 42px; font-family: "Tinos", "Times New Roman", serif; font-size: 15px; color: var(--white); }
  .footer-links { position: absolute; left: 209px; top: 66px; font-family: "Roboto Condensed", "Arial Narrow", sans-serif; font-size: 12.5px; color: var(--white); white-space: nowrap; }
</style>
</head>
<body>
  <header class="header">
    <div class="brand"><span class="brand-mark"></span><span class="brand-name">QUILLMERE</span></div>
    <nav class="utility-nav">
      <a href="#">Group Companies</a><a href="#">Employment &amp; Association</a><a href="#">Divisions</a>
    </nav>
  </header>

  <nav class="main-nav">
    <ul>
      <li class="current">Home</li>
      <li class="soft">About the Group</li>
      <li>Chairman's Message</li>
      <li>Contact us</li>
    </ul>
  </nav>

  <section class="hero">
    <div class="hero-visual" role="img" aria-label="Photo of a tall modern residential tower against a blue sky"></div>
    <h1 class="hero-title">Lorem ipsum dolor sit</h1>
    <p class="hero-sub">Lorem ipsum dolor sit amet, consectetur adipiscing elit.</p>
    <p class="hero-text">Lorem ipsum dolor sit amet, consectetur adipiscing elit. Donec ut metus id nisi consectetur<br>faucibus. Vestibulum rhoncus consectetur justo, sit amet volutpat</p>
    <div class="hero-rule"></div>
    <div class="hero-btn prev">
      <svg width="14" height="12" viewBox="0 0 14 12"><path d="M7 0 L1 6 L7 12Z M13 0 L7 6 L13 12Z" fill="#eee"/></svg>
    </div>
    <div class="hero-btn all">See all Projects</div>
    <div class="hero-btn next">
      <svg width="14" height="12" viewBox="0 0 14 12"><path d="M1 0 L7 6 L1 12Z M7 0 L13 6 L7 12Z" fill="#eee"/></svg>
    </div>
  </section>

  <h2 class="abs heading blue" style="left:208px">Employment &amp; Alliances</h2>
  <p class="abs copy top" style="left:206px">Lorem ipsum dolor sit amet, consectetur adipiscing<br>elit. Fusce eget leo nunc. Fusce posuere erat eget<br>mi porttitor eleifend. Lorem ipsum dolor sit amet,<br>consectetur adipiscing elit.</p>
  <div class="abs tab" style="left:210px">Empoly &amp; alliance</div>
  <div class="abs photo team" style="left:210px" role="img" aria-label="Photo of business professionals in an office meeting"></div>
  <p class="abs copy bottom" style="left:210px">Lorem ipsum dolor sit amet, consectetur adipiscing<br>elit. Fusce eget leo nunc. Fusce posuere erat eget<br>mi porttitor eleifend. Lorem ipsum dolor sit amet,<br>consectetur adipiscing elit. Morbi vulputate</p>
  <div class="abs read-more" style="left:265px">Read more</div>

  <div class="abs divider" style="left:475px"></div>

  <h2 class="abs heading" style="left:494px">Legal Consultation</h2>
  <p class="abs copy top" style="left:496px">Lorem ipsum dolor sit amet, consectetur adipiscing<br>elit. Fusce eget leo nunc. Fusce posuere erat eget<br>mi porttitor eleifend. Lorem ipsum dolor sit amet,<br>consectetur adipiscing elit.</p>
  <div class="abs tab" style="left:495px">Consulting</div>
  <div class="abs photo deal" style="left:495px" role="img" aria-label="Photo of a business handshake in front of office towers"></div>
  <p class="abs copy bottom" style="left:496px">Lorem ipsum dolor sit amet, consectetur adipiscing<br>elit. Fusce eget leo nunc. Fusce posuere erat eget<br>mi porttitor eleifend. Lorem ipsum dolor sit amet,<br>consectetur adipiscing elit.</p>
  <div class="abs read-more" style="left:570px">Read more</div>

  <div class="abs divider" style="left:760px"></div>

  <h2 class="abs heading" style="left:779px">Services</h2>
  <ul class="abs services">
    <li>Legal Services</li>
    <li>Media Production</li>
    <li>Real Estate Investment</li>
    <li class="cont">&amp; Management</li>
    <li>General Trading</li>
    <li>Business Services</li>
    <li>Telecommunication</li>
    <li class="cont">Products &amp; Services</li>
  </ul>
  <div class="abs services-rule"></div>
  <h3 class="abs heading" style="left:781px; top:851px">Contact us</h3>
  <div class="abs contact-row" style="top:899px">Telephone:<span>+971 4 555 0142</span></div>
  <div class="abs contact-row" style="top:933px">Fax:<span>+971 4 555 0143</span></div>
  <div class="abs contact-row" style="top:967px">Email:<span>info@quillmere-example.com</span></div>

  <footer class="footer">
    <div class="footer-name">Quillmere group Company</div>
    <div class="footer-links">© 2012 &nbsp;Quillmere group , About Us, Project's, Portfolio, Gallery, Contact Us, Career.</div>
  </footer>
</body>
</html>
```